Shine Barn Auto Care Business Card

2 side business card design for an auto detailing business

Target Market(s)

Auto detailing

Contact Information for Business Card

Things included

The business name “Shine Barn Auto Care”
Owen Marchetti
(403)871-2964
Maplecrest, Sk

Services offered - complete interior& exterior detail
- paint correction & protection
- ceramic coating
- trim restore
- auto carpet & seat cleaning

Requirements
Must have
• Colours that are in my logo

Services offered

My name Owen Marchetti
403-871-2964
Maplecrest, Sk

Not too sure in what order for these ?
Website. Shinebarnautocare.com
Instagram Shinebarnautocare
Email. Shinebarnautoac@mailbox-example.com

```html
<!DOCTYPE html>
<html lang="en">
<head>
<meta charset="utf-8">
<title>Shine Barn Auto Care – Business Card</title>
<link href="https://fonts.googleapis.com/css2?family=Open+Sans:wght@400;600;700&display=swap" rel="stylesheet">
<style>
  :root {
    --brand-red: #971b20;
    --brand-red-dark: #7d1519;
    --ink: #1a1a1a;
    --grey-text: #5a5a5a;
    --paper: #ffffff;
    --backdrop: #dcdcda;
  }
  * { box-sizing: border-box; margin: 0; padding: 0; }
  html, body {
    width: 1200px; height: 801px; overflow: hidden;
    background: var(--backdrop);
    font-family: "Open Sans", Arial, sans-serif;
  }
  .sheet { position: relative; width: 1200px; height: 801px; }
  .card {
    position: absolute; left: 290px; width: 620px; height: 354px;
    overflow: hidden; box-shadow: 0 6px 18px rgba(0,0,0,.18);
  }
  .card--front { top: 30px; background: var(--paper); }
  .card--back { top: 417px; background: var(--brand-red); }

  .front-wave { position: absolute; inset: 0; }

  .brand { position: absolute; left: 40px; top: 112px; width: 210px; text-align: center; }
  .brand__mark {
    width: 64px; height: 64px; border-radius: 50%;
    background: var(--brand-red); margin: 0 auto 14px;
  }
  .brand__name {
    font-weight: 700; font-size: 19px; color: var(--ink); line-height: 1.2;
  }

  .divider {
    position: absolute; left: 268px; top: 92px; width: 1px; height: 148px;
    background: var(--brand-red);
  }

  .contact { position: absolute; left: 288px; top: 86px; }
  .contact__name {
    font-weight: 700; font-size: 21px; color: var(--brand-red); letter-spacing: .3px;
  }
  .contact__role { font-size: 14px; color: var(--grey-text); margin-bottom: 12px; }
  .contact__list { list-style: none; }
  .contact__item {
    display: flex; align-items: center; gap: 8px;
    font-size: 13px; color: var(--grey-text); line-height: 22px;
  }
  .contact__icon { width: 12px; height: 12px; flex: none; fill: var(--brand-red); }
  .contact__dot { width: 10px; height: 10px; border-radius: 50%; background: var(--brand-red); flex: none; margin: 0 1px; }

  .website {
    position: absolute; right: 26px; bottom: 14px;
    font-size: 14px; color: var(--paper); transform: rotate(-4deg);
  }

  .back-brand { position: absolute; left: 0; right: 0; top: 86px; text-align: center; }
  .back-brand__mark {
    width: 100px; height: 100px; border-radius: 50%;
    background: var(--brand-red-dark); margin: 0 auto 10px;
  }
  .back-brand__name { font-weight: 700; font-size: 15px; color: var(--brand-red-dark); }

  .services {
    position: absolute; left: 40px; right: 40px; bottom: 38px;
    text-align: center; color: var(--paper); font-size: 15px; line-height: 24px;
  }
</style>
</head>
<body>
<main class="sheet">
  <section class="card card--front" aria-label="Card front">
    <svg class="front-wave" viewBox="0 0 620 354" preserveAspectRatio="none" aria-hidden="true">
      <path d="M90 354 C220 330 300 300 380 270 C470 238 540 250 620 228 L620 354 Z" fill="#971b20"/>
      <path d="M90 354 C220 326 300 288 380 256 C470 222 540 232 620 208 L620 228 C540 250 470 238 380 270 C300 300 220 330 90 354 Z" fill="#111"/>
    </svg>

    <div class="brand">
      <div class="brand__mark"></div>
      <p class="brand__name">Shine Barn Auto Care</p>
    </div>

    <div class="divider"></div>

    <div class="contact">
      <h1 class="contact__name">OWEN MARCHETTI</h1>
      <p class="contact__role">President</p>
      <ul class="contact__list">
        <li class="contact__item">
          <svg class="contact__icon" viewBox="0 0 24 24"><path d="M6.6 10.8a15 15 0 0 0 6.6 6.6l2.2-2.2a1 1 0 0 1 1-.25 11.4 11.4 0 0 0 3.6.6 1 1 0 0 1 1 1V20a1 1 0 0 1-1 1A17 17 0 0 1 3 4a1 1 0 0 1 1-1h3.5a1 1 0 0 1 1 1c0 1.25.2 2.45.6 3.6a1 1 0 0 1-.25 1z"/></svg>
          403-871-2964
        </li>
        <li class="contact__item">
          <svg class="contact__icon" viewBox="0 0 24 24"><path d="M2 5h20v14H2z" fill="#971b20"/><path d="M3 6l9 7 9-7" fill="none" stroke="#fff" stroke-width="1.6"/></svg>
          Shinebarnautoac@mailbox-example.com
        </li>
        <li class="contact__item">
          <span class="contact__dot"></span>
          Shinebarnautocare
        </li>
        <li class="contact__item">
          <svg class="contact__icon" viewBox="0 0 24 24"><path d="M12 2a7 7 0 0 0-7 7c0 5 7 13 7 13s7-8 7-13a7 7 0 0 0-7-7zm0 9.5A2.5 2.5 0 1 1 12 6.5a2.5 2.5 0 0 1 0 5z"/></svg>
          Maplecrest, Sk
        </li>
      </ul>
    </div>

    <p class="website">Shinebarnautocare.com</p>
  </section>

  <section class="card card--back" aria-label="Card back">
    <div class="back-brand">
      <div class="back-brand__mark"></div>
      <p class="back-brand__name">Shine Barn Auto Care</p>
    </div>
    <p class="services">
      complete interior&amp; exterior detail &nbsp;•&nbsp; paint correction &amp; protection<br>
      ceramic coating &nbsp;•&nbsp; trim restore &nbsp;•&nbsp; auto carpet &amp; seat cleaning
    </p>
  </section>
</main>
</body>
</html>
```